Cloud Based Internet Protection Service Business Cards

I would like a professionally designed business card. I already have a logo which I have attached.

The business is an online cloud based internet protection service aimed parents, particularly at non-technical parents and also schools.

The card should be be quite simple in its design, not to full of text and give its information in a clear and concise manner

Target Market(s)

Parents (especially non-technical parents) and also schools

Industry/Entity Type

Internet

Colors

Designer to choose colors to be used in the design.

Requirements
Should not have
• Too much text or be too cluttered. No decorative fonts, just a clear and concise font.

```html
<!DOCTYPE html>
<html lang="en">
<head>
<meta charset="utf-8">
<title>SafeNest Business Card</title>
<link href="https://fonts.googleapis.com/css2?family=Open+Sans:wght@400;600;700&display=swap" rel="stylesheet">
<style>
  :root{
    --backdrop:#2b2d31;
    --card-white:#ffffff;
    --navy:#0d3f5e;
    --teal:#0f5f80;
    --wave-light:#5b95d1;
    --muted-blue:#6a9fd0;
    --ink:#1b3e57;
    --back-top:#5f93c4;
    --back-bottom:#3c6c9e;
  }
  *{margin:0;padding:0;box-sizing:border-box}
  html,body{width:1200px;height:720px;overflow:hidden}
  body{
    background:var(--backdrop);
    font-family:"Open Sans",Arial,sans-serif;
    display:flex;align-items:center;justify-content:center;gap:40px;
  }
  .card{
    position:relative;width:530px;height:303px;overflow:hidden;
    box-shadow:0 10px 30px rgba(0,0,0,.35);
  }
  .card--front{background:var(--card-white)}
  .front-wave{position:absolute;inset:0;width:100%;height:100%}
  .brand{
    position:absolute;left:168px;top:40px;
    display:flex;align-items:center;gap:10px;
    font-weight:700;font-size:30px;color:var(--teal);letter-spacing:.5px;
  }
  .brand__dot{width:18px;height:18px;border-radius:50%;background:var(--teal)}
  .person{position:absolute;left:300px;top:118px}
  .person__name{font-weight:700;font-size:25px;color:var(--teal);line-height:1.1}
  .person__role{font-size:14px;color:var(--muted-blue);margin-top:2px}
  .contacts{position:absolute;left:300px;top:180px;list-style:none}
  .contacts li{display:flex;align-items:center;gap:10px;font-size:14px;color:var(--ink);line-height:24px}
  .contacts li.web{font-weight:700}
  .contacts svg{width:14px;height:14px;flex:none}
  .card--back{
    background:linear-gradient(160deg,var(--back-top),var(--back-bottom));
    display:flex;align-items:center;justify-content:center;
  }
  .back-brand{
    display:flex;align-items:center;gap:16px;
    font-weight:700;font-size:56px;color:#ffffff;letter-spacing:1px;
  }
  .back-brand__dot{width:34px;height:34px;border-radius:50%;background:#ffffff}
</style>
</head>
<body>
  <section class="card card--front">
    <svg class="front-wave" viewBox="0 0 530 303" preserveAspectRatio="none" aria-hidden="true">
      <path d="M0 0 H110 C150 90 120 200 220 303 H0 Z" fill="var(--wave-light)"/>
      <path d="M0 0 H90 C130 95 95 200 190 303 H0 Z" fill="var(--navy)"/>
    </svg>
    <div class="brand"><span class="brand__dot"></span>SafeNest</div>
    <div class="person">
      <p class="person__name">Dana Whitfield</p>
      <p class="person__role">Managing Member</p>
    </div>
    <ul class="contacts">
      <li><svg viewBox="0 0 16 16"><path d="M3 2h3l1 4-2 1c1 2 2 3 4 4l1-2 4 1v3c0 1-1 1-2 1C7 14 2 9 2 4c0-1 0-2 1-2z" fill="var(--muted-blue)"/></svg>555-210-400</li>
      <li><svg viewBox="0 0 16 16"><rect x="4" y="1" width="8" height="14" rx="1.5" fill="var(--muted-blue)"/><rect x="5.5" y="3" width="5" height="8" fill="#fff"/></svg>555-318-627</li>
      <li><svg viewBox="0 0 16 16"><rect x="1" y="3" width="14" height="10" rx="1" fill="var(--muted-blue)"/><path d="M1.5 3.5 8 9l6.5-5.5" stroke="#fff" stroke-width="1.3" fill="none"/></svg>hello@safenest.com</li>
      <li class="web"><svg viewBox="0 0 16 16"><circle cx="8" cy="8" r="7" fill="var(--muted-blue)"/><path d="M1 8h14M8 1c-3 3-3 11 0 14M8 1c3 3 3 11 0 14" stroke="#fff" stroke-width="1" fill="none"/></svg>www.safenest.com</li>
    </ul>
  </section>

  <section class="card card--back">
    <div class="back-brand"><span class="back-brand__dot"></span>SafeNest</div>
  </section>
</body>
</html>
```